Silver Heron Staffing Agency

I need to make a brochure/catalogue that represent our company, telling our clients what we do, our values, fields of industry that we taken care of, so they know who we are, what we did, and how we do it.
I do have a logo and simple brochure design before that i really need to upgrade (i will give it as an example on this attachment).

What I want in the new design is :
1. More pictures and little bit of explanation in each industry we work with.
2. Attractive design that make people LOOK at the brochure and not just throw it in the trash.
3. Still use the combination color of the company logo itself, which is Golden Brown.

```html
<!DOCTYPE html>
<html lang="en">
<head>
<meta charset="utf-8">
<title>Silver Heron Staffing Agency – Trifold Brochure</title>
<link href="https://fonts.googleapis.com/css2?family=Montserrat:wght@400;500;600;700;800&display=swap" rel="stylesheet">
<style>
:root{
  --backdrop:#7d8082;
  --black:#0a0a0a;
  --ink:#141414;
  --gold:#c9a54a;
  --gold-deep:#a9852f;
  --gold-pale:#e4d08e;
  --white:#ffffff;
  --paper:#efefef;
  --paper-shade:#d6d6d6;
  --text-light:#e8e8e8;
  --text-dark:#1b1b1b;
}
*{box-sizing:border-box;margin:0;padding:0}
html,body{width:1200px;height:2400px;overflow:hidden}
body{background:var(--backdrop);font-family:'Montserrat',sans-serif;position:relative}
.spread{position:absolute;left:60px;width:1080px;height:836px;background:var(--black);box-shadow:0 6px 18px rgba(0,0,0,.35);overflow:hidden}
.spread--outside{top:324px}
.spread--inside{top:1240px}
.panel{position:absolute;top:0;width:360px;height:836px}
.panel--1{left:0}.panel--2{left:360px}.panel--3{left:720px}
.abs{position:absolute}
.heading{font-weight:800;font-size:18px;letter-spacing:.2px;text-transform:uppercase}
.heading--gold{color:var(--gold)}
.heading--dark{color:var(--ink)}
.rule{position:absolute;height:1px;width:110px;background:var(--gold)}
.body-copy{font-size:10.6px;line-height:13.1px;text-align:justify}
.body-copy--light{color:var(--text-light)}
.body-copy--dark{color:var(--text-dark)}
.photo{position:absolute}

/* outside – gold panel */
.panel--location{background:linear-gradient(180deg,#b18c36 0%,#c6a351 45%,#e2cc86 100%)}
.location-list{position:absolute;top:102px;left:40px;width:300px;display:grid;grid-template-columns:155px 145px;row-gap:10px}
.location-item{display:flex;align-items:center;gap:8px;color:var(--white);font-size:13px;font-weight:500}
.location-badge{width:34px;height:34px;border-radius:50%;border:2px solid var(--white);display:flex;align-items:center;justify-content:center}
.location-badge span{width:10px;height:10px;border-radius:50%;background:var(--white)}
.call-title{top:302px;width:360px;text-align:center;font-weight:800;font-size:17px;color:var(--ink)}
.phone-pill{top:337px;left:46px;width:268px;height:52px;border-radius:12px;background:var(--black);color:var(--white);font-weight:800;font-size:29px;letter-spacing:1px;display:flex;align-items:center;justify-content:center}
.contact-icon{left:172px;width:16px;height:16px}
.contact-line{width:360px;text-align:center;color:var(--white);font-size:13px;line-height:16px}
.contact-rule{left:115px;width:130px;height:1px;background:var(--ink)}
.brand-lockup{display:flex;align-items:center;gap:10px;font-weight:700;letter-spacing:.5px}
.brand-lockup .mark{width:24px;height:24px;border-radius:50%}
.brand-lockup--location{top:720px;left:0;width:360px;justify-content:center;color:var(--ink);font-size:20px}
.brand-lockup--location .mark{background:var(--ink)}

/* outside – cover */
.brand-lockup--cover{top:95px;left:0;width:360px;justify-content:center;color:var(--gold);font-size:22px}
.brand-lockup--cover .mark{background:var(--gold)}
.cover-headline{top:640px;width:360px;text-align:center;color:var(--gold);font-weight:800;font-size:31px;line-height:39px}
.cover-web{top:784px;width:360px;text-align:center;color:var(--white);font-size:13.5px;letter-spacing:.3px}

/* inside */
.paper-top{position:absolute;left:0;top:0;width:720px;height:426px;background:linear-gradient(180deg,var(--paper) 0%,#e4e4e4 50%,var(--paper-shade) 100%)}
.industry-icons{position:absolute;left:0;width:360px}
.industry{position:absolute;width:90px;margin-left:-45px;text-align:center}
.industry-ring{width:48px;height:48px;margin:0 auto;border-radius:50%;border:2px solid var(--gold);display:flex;align-items:center;justify-content:center}
.industry-label{margin-top:8px;color:var(--white);font-weight:700;font-size:9.5px;white-space:nowrap}
.industry-lead{color:var(--white);font-weight:700;font-size:12.5px;line-height:15px}
</style>
</head>
<body>

<!-- Outside spread -->
<section class="spread spread--outside">

  <div class="panel panel--1">
    <h2 class="heading heading--gold abs" style="top:50px;left:24px">About Us</h2>
    <div class="rule" style="top:79px;left:24px"></div>
    <p class="body-copy body-copy--light abs" style="top:95px;left:24px;width:305px">With more than 18 years of experience Silver Heron Staffing provided staffing services to a wide array of locations, all throughout Pennsylvania. Through the last few years we have expanded to 5 other states including New York, New Jersey, Delaware, Virginia and Georgia. Our ethics are a critical building block of our business. Our own success is based on adherence to the highest ethical standards; long-term client relationships, the ability to identify top candidates, and the high-quality professional development of Silver Heron Staffing professionals protecting the confidentiality and interests of clients and candidates.</p>
    <div class="photo" role="img" aria-label="Hand selecting a highlighted person within a network of connected people icons" style="top:284px;left:0;width:360px;height:310px;background:linear-gradient(160deg,#c9c9c9 0%,#6b5a55 35%,#2a2222 70%,#0a0a0a 100%)"></div>
    <h2 class="heading heading--gold abs" style="top:602px;left:24px">Why Us?</h2>
    <div class="rule" style="top:630px;left:24px"></div>
    <p class="body-copy body-copy--light abs" style="top:644px;left:24px;width:305px">With more than 18 years of experience Silver Heron Staffing provided staffing services to a wide array of locations, all throughout Pennsylvania. Through the last few years we have expanded to 5 other states including New York, New Jersey, Delaware, Virginia and Georgia. Our ethics are a critical building block of our business. Our own success is based on adherence to the highest ethical standards; long-term client relationships, the ability to identify top candidates, and the high-quality professional development of Silver Heron Staffing professionals protecting the confidentiality and interests of clients and candidates.</p>
  </div>

  <div class="panel panel--2 panel--location">
    <h2 class="heading heading--dark abs" style="top:54px;width:360px;text-align:center">Our Location</h2>
    <div class="location-list">
      <div class="location-item"><div class="location-badge"><span></span></div>New York</div>
      <div class="location-item"><div class="location-badge"><span></span></div>Delaware</div>
      <div class="location-item"><div class="location-badge"><span></span></div>Pensylvania</div>
      <div class="location-item"><div class="location-badge"><span></span></div>Verginia</div>
      <div class="location-item"><div class="location-badge"><span></span></div>New jersey</div>
      <div class="location-item"><div class="location-badge"><span></span></div>Georgia</div>
    </div>
    <div class="call-title abs">CALL US TODAY</div>
    <div class="phone-pill abs">555-014-2760</div>

    <svg class="contact-icon abs" style="top:412px" viewBox="0 0 16 16"><rect x="1" y="3" width="14" height="10" fill="var(--ink)"/><path d="M1 3 L8 9 L15 3" fill="none" stroke="#c6a351" stroke-width="1.3"/></svg>
    <div class="contact-line abs" style="top:432px">info@silverheronstaffing.com</div>
    <div class="contact-rule abs" style="top:455px"></div>

    <svg class="contact-icon abs" style="top:474px" viewBox="0 0 16 16"><path d="M8 1 C4.7 1 3 3.5 3 6 C3 9.5 8 15 8 15 C8 15 13 9.5 13 6 C13 3.5 11.3 1 8 1Z" fill="var(--ink)"/><circle cx="8" cy="6" r="2" fill="#c9a651"/></svg>
    <div class="contact-line abs" style="top:496px">42 Alder Ln, suite 310<br>Riverton, NJ 08077</div>
    <div class="contact-rule abs" style="top:536px"></div>

    <svg class="contact-icon abs" style="top:556px" viewBox="0 0 16 16"><circle cx="8" cy="8" r="6.5" fill="none" stroke="var(--ink)" stroke-width="1.5"/><ellipse cx="8" cy="8" rx="3" ry="6.5" fill="none" stroke="var(--ink)" stroke-width="1.2"/><line x1="1.5" y1="8" x2="14.5" y2="8" stroke="var(--ink)" stroke-width="1.2"/></svg>
    <div class="contact-line abs" style="top:578px">www.silverheronstaffing.com</div>
    <div class="contact-rule abs" style="top:600px"></div>

    <div class="brand-lockup brand-lockup--location abs"><span class="mark"></span>SILVER HERON Inc.</div>
  </div>

  <div class="panel panel--3">
    <div class="brand-lockup brand-lockup--cover abs"><span class="mark"></span>SILVER HERON Inc.</div>
    <div class="photo" role="img" aria-label="Smiling manager in a blue shirt and striped tie holding a clipboard in a warehouse" style="top:203px;left:0;width:360px;height:412px;background:linear-gradient(180deg,#0a0a0a 0%,#3a3024 40%,#7a6a58 75%,#4a4a58 100%)"></div>
    <div class="cover-headline abs">WE MAKE<br>FINDING GREAT<br>PEOPLE EASY</div>
    <div class="cover-web abs">www.silverheronstaffing.com</div>
  </div>
</section>

<!-- Inside spread -->
<section class="spread spread--inside">
  <div class="paper-top"></div>

  <div class="panel panel--1">
    <h2 class="heading heading--dark abs" style="top:42px;left:26px">Our Story</h2>
    <div class="rule" style="top:69px;left:26px"></div>
    <p class="body-copy body-copy--dark abs" style="top:80px;left:26px;width:305px">With more than 18 years of experience Silver Heron Staffing has provided staffing services all throughout Pennsylvania, New York, New Jersey, Delaware, Virginia &amp; Georgia.<br><br>Our success is based on our unique ability to identify top candidates and the high-quality professional development of our candidates.</p>
    <h2 class="heading heading--gold abs" style="top:456px;left:26px">Our Mission</h2>
    <div class="rule" style="top:483px;left:26px"></div>
    <p class="body-copy body-copy--light abs" style="top:492px;left:26px;width:305px">Silver Heron Staffing is more than a staffing company; we want to become your business partner. We understand that payroll and employee-service overhead can be one of the largest expenses for your business. Through our partnership-network programs Silver Heron Staffing can help you reduce the hard-costs of your business expenses. We take responsibility for all our placed employees, including payroll taxes and benefits allowing you to focus on running your business.</p>
  </div>

  <div class="photo" role="img" aria-label="Row of eight smiling workers in different uniforms: industrial, medical, construction, photography, hospitality and retail" style="top:231px;left:0;width:720px;height:195px;background:linear-gradient(90deg,#1e2a3a 0%,#2a7a8a 14%,#b8232a 28%,#e0e0e0 40%,#151515 52%,#7cc05a 64%,#b01e24 78%,#e6e83a 92%,#1d2a4a 100%)"></div>

  <div class="panel panel--2">
    <h2 class="heading heading--dark abs" style="top:42px;left:30px">Our Culture</h2>
    <div class="rule" style="top:69px;left:30px"></div>
    <p class="body-copy body-copy--dark abs" style="top:80px;left:30px;width:305px">Silver Heron Staffing believes in equal opportunity for all, regardless of gender, race, ethic, origin, religion, or handicap. The staffing policies and practices of Silver Heron Staffing for our organization, our clients and candidates are fully non-discriminatory. Our employees are our most valuable asset. We strive to create a work environment of professionalism, trust and respect that will continuously provide our staff with motivation, challenge, and professional growth to aim our most important goal; CLIENT SATISFACTION.</p>
    <h2 class="heading heading--gold abs" style="top:490px;left:22px">Our Process</h2>
    <div class="rule" style="top:517px;left:22px"></div>
    <p class="body-copy body-copy--light abs" style="top:526px;left:22px;width:318px">Our screening process includes a thorough interview with each potential candidate to give us insight into the candidate's previous work history, skills, communication abilities and career goals as well as reference checks with their previous employers.</p>
  </div>

  <div class="panel panel--3">
    <div class="photo" role="img" aria-label="Hand touching a glowing people icon in a circle of contacts on a blue background" style="top:28px;left:22px;width:308px;height:217px;background:radial-gradient(circle at 50% 45%,#6fd3ef 0%,#1f9cc6 45%,#0a4a70 100%)"></div>
    <h2 class="heading heading--gold abs" style="top:262px;left:18px">Industries We Serve</h2>
    <p class="body-copy body-copy--light abs" style="top:294px;left:18px;width:310px">Need industry-leading talent for your organization? Career options that are ideal for your skills and experience? The professionals at Silver Heron Staffing have the tools and knowledge to help you make the perfect match.</p>
    <p class="industry-lead abs" style="top:366px;left:18px;width:300px">Our specialties include staffing for the following industries:</p>

    <div class="industry-icons" style="top:430px">
      <div class="industry" style="left:60px;top:0">
        <div class="industry-ring"><svg width="24" height="24" viewBox="0 0 24 24"><path d="M2 10 L12 3 L22 10 V21 H2Z" fill="var(--gold)"/><rect x="7" y="12" width="10" height="9" fill="var(--black)"/><path d="M7 15 H17 M7 18 H17" stroke="var(--gold)"/></svg></div>
        <div class="industry-label">WAREHOUSING</div>
      </div>
      <div class="industry" style="left:142px;top:0">
        <div class="industry-ring"><svg width="24" height="24" viewBox="0 0 24 24"><rect x="5" y="3" width="14" height="18" fill="var(--gold)"/><g fill="var(--black)"><rect x="8" y="6" width="2" height="2"/><rect x="14" y="6" width="2" height="2"/><rect x="8" y="11" width="2" height="2"/><rect x="14" y="11" width="2" height="2"/><rect x="10.5" y="16" width="3" height="5"/></g></svg></div>
        <div class="industry-label">HOTEL</div>
      </div>
      <div class="industry" style="left:224px;top:0">
        <div class="industry-ring"><svg width="24" height="24" viewBox="0 0 24 24"><rect x="3" y="6" width="10" height="10" rx="1.5" fill="var(--gold)" transform="rotate(-12 8 11)"/><rect x="11" y="9" width="10" height="10" rx="1.5" fill="var(--gold)" transform="rotate(14 16 14)"/><circle cx="8" cy="11" r="1.2" fill="var(--black)"/><circle cx="16" cy="14" r="1.2" fill="var(--black)"/></svg></div>
        <div class="industry-label">CASINO</div>
      </div>
      <div class="industry" style="left:305px;top:0">
        <div class="industry-ring"><svg width="24" height="24" viewBox="0 0 24 24"><path d="M2 20 L9 12 L13 16 L16 12 L22 20Z" fill="var(--gold)"/><path d="M12 4 L19 4 L19 9" fill="none" stroke="var(--gold)" stroke-width="2"/></svg></div>
        <div class="industry-label">LANDFILL</div>
      </div>

      <div class="industry" style="left:67px;top:97px">
        <div class="industry-ring"><svg width="26" height="24" viewBox="0 0 26 24"><rect x="2" y="6" width="14" height="11" fill="var(--gold)"/><path d="M16 9 H21 L24 13 V17 H16Z" fill="var(--gold)"/><circle cx="7" cy="18.5" r="2.5" fill="var(--gold)" stroke="var(--black)"/><circle cx="19" cy="18.5" r="2.5" fill="var(--gold)" stroke="var(--black)"/></svg></div>
        <div class="industry-label">TRANSPORTATION</div>
      </div>
      <div class="industry" style="left:178px;top:97px">
        <div class="industry-ring"><svg width="24" height="24" viewBox="0 0 24 24"><rect x="6" y="3" width="12" height="18" fill="var(--gold)"/><path d="M8.5 7 H15.5 M8.5 10 H15.5 M8.5 13 H15.5 M8.5 16 H13" stroke="var(--black)" stroke-width="1.2"/></svg></div>
        <div class="industry-label">PAPER MAILING</div>
      </div>
      <div class="industry" style="left:288px;top:97px">
        <div class="industry-ring"><svg width="24" height="24" viewBox="0 0 24 24"><path d="M7 3 V21 M5 3 V9 M9 3 V9 M5 9 H9" stroke="var(--gold)" stroke-width="1.8" fill="none"/><path d="M16 3 C19 5 19 11 16 12 V21" stroke="var(--gold)" stroke-width="2" fill="none"/></svg></div>
        <div class="industry-label">FOOD HANDLING</div>
      </div>
    </div>
  </div>

  <div class="photo" role="img" aria-label="Warehouse worker in hard hat and safety vest with a clipboard" style="top:632px;left:26px;width:248px;height:174px;background:linear-gradient(160deg,#8a6a50 0%,#c9b25a 50%,#3a3a44 100%)"></div>
  <div class="photo" role="img" aria-label="Hotel housekeeper with a service cart in a hallway" style="top:632px;left:283px;width:248px;height:174px;background:linear-gradient(160deg,#f0ece6 0%,#c98a5a 50%,#7a2a20 100%)"></div>
  <div class="photo" role="img" aria-label="Casino dealer in a vest at a gaming table with guests" style="top:632px;left:540px;width:248px;height:174px;background:linear-gradient(160deg,#d0d0d0 0%,#3a3030 45%,#8a2a20 100%)"></div>
  <div class="photo" role="img" aria-label="Smiling driver at the steering wheel of a car" style="top:632px;left:797px;width:248px;height:174px;background:linear-gradient(160deg,#e8e8e8 0%,#6a6a6a 45%,#151515 100%)"></div>
</section>

</body>
</html>
```